依頼詳細
不動産の案内所や現地、宣伝用に置けるような「のぼり旗」を作成したいと思います。
観光スポットなどをドライブしながらでも違和感のない感じだとありがたいです。
目には止まって欲しいけどリゾート地に設置したいのでカチカチなデザインでない方が良いです。
記載項目
碧浜ソレイユ、ロゴ、0995−61−2348、
※海が見える売土地あります

※この部分は変えられるようにしたいです。
・海が見える売物件
・管理地
・不動産案内所
・売地募集中
・不動産のことならお気軽にどうぞ
希望イメージ
シンプル 複雑
単色 カラフル
暗い 明るい
日常 高級
遊び心 厳粛
未来的 伝統的
女性的 男性的
希望する色
青系、水色系
納品ファイル
• イラストレーター形式 (.ai)
補足説明
その他、掲載した方が良い文字や表現などありましたら追加していただいて大丈夫です。
サイズを掲載するのを忘れましたが標準の横600×縦1800mmで考えております。
中身の文字は臨機応変に変更しようかと思っております。
よろしくお願いいたします。
■ 選んだ理由

リゾート地に設置した際にイメージに合いながらも目を引きそうな感じがとても気に入りました。

■ 提案者全員のお礼・コメント

とても素敵なデザインありがとうございました!!
貴重なお時間をかけて考えていただき感謝いたします。
また機会がありましたらぜひよろしくお願いいたします。

```html
<!DOCTYPE html>
<html lang="ja">
<head>
<meta charset="utf-8">
<title>海が見える売土地あります｜碧浜ソレイユ</title>
<link href="https://fonts.googleapis.com/css2?family=M+PLUS+Rounded+1c:wght@500;700;800&display=swap" rel="stylesheet">
<style>
  :root {
    --sky: #c0e4f8;
    --sea-mid: #9fd3f0;
    --sea-deep: #7fc3ea;
    --ink: #0b5aa8;
    --white: #ffffff;
  }
  * { margin: 0; padding: 0; box-sizing: border-box; }
  html, body { width: 1200px; height: 3602px; overflow: hidden; background: var(--white); }
  .banner {
    position: relative;
    width: 1200px;
    height: 3602px;
    overflow: hidden;
    background: var(--white);
    font-family: "M PLUS Rounded 1c", sans-serif;
    color: var(--ink);
  }
  .banner__sky {
    position: absolute; left: 0; top: 0;
    width: 1200px; height: 2000px;
    background: var(--sky);
  }
  .banner__waves {
    position: absolute; left: 0; top: 1880px;
    width: 1200px; height: 1000px;
  }
  .headline {
    position: absolute;
    top: 160px;
    width: 340px;
    display: flex;
    flex-direction: column;
    align-items: center;
    font-weight: 700;
  }
  .headline__char {
    display: block;
    width: 340px;
    text-align: center;
    white-space: nowrap;
  }
  .headline--lead { left: 650px; }
  .headline--lead .headline__char {
    font-size: 262px;
    height: 304px;
    line-height: 304px;
  }
  .headline--main { left: 222px; }
  .headline--main .headline__char {
    font-size: 270px;
    height: 316px;
    line-height: 316px;
  }
  .brand-mark {
    position: absolute;
    left: 0; top: 2740px;
    width: 1200px;
    display: flex;
    flex-direction: column;
    align-items: center;
    gap: 40px;
  }
  .brand-mark__dot {
    width: 150px; height: 150px;
    border-radius: 50%;
    background: var(--ink);
  }
  .brand-mark__name {
    font-size: 92px;
    font-weight: 800;
    color: var(--ink);
    letter-spacing: 4px;
    line-height: 1.1;
  }
  .company {
    position: absolute;
    left: 0; top: 3255px;
    width: 1200px;
    text-align: center;
    font-size: 86px;
    font-weight: 800;
    letter-spacing: 2px;
    line-height: 1.2;
  }
  .contact-bar {
    position: absolute;
    left: 0; top: 3398px;
    width: 1200px; height: 204px;
    background: var(--ink);
    color: var(--white);
    display: flex;
    align-items: center;
    justify-content: center;
    gap: 18px;
  }
  .contact-bar__icon { width: 100px; height: 80px; }
  .contact-bar__number {
    font-size: 116px;
    font-weight: 800;
    letter-spacing: 2px;
    line-height: 1;
  }
</style>
</head>
<body>
  <main class="banner">
    <div class="banner__sky"></div>

    <svg class="banner__waves" role="img" aria-label="波しぶきと泡、泳ぐ小魚のイラスト" viewBox="0 0 1200 1000" preserveAspectRatio="none">
      <defs>
        <linearGradient id="seaFade" x1="0" y1="0" x2="0" y2="1">
          <stop offset="0" stop-color="#c0e4f8"/>
          <stop offset="0.35" stop-color="#9fd3f0"/>
          <stop offset="0.6" stop-color="#dff1fb"/>
          <stop offset="0.85" stop-color="#ffffff"/>
          <stop offset="1" stop-color="#ffffff"/>
        </linearGradient>
      </defs>
      <rect x="0" y="0" width="1200" height="1000" fill="url(#seaFade)"/>
    </svg>

    <h1 class="headline headline--lead" aria-label="海が見える">
      <span class="headline__char">海</span>
      <span class="headline__char">が</span>
      <span class="headline__char">見</span>
      <span class="headline__char">え</span>
      <span class="headline__char">る</span>
    </h1>
    <h2 class="headline headline--main" aria-label="売土地あります">
      <span class="headline__char">売</span>
      <span class="headline__char">土</span>
      <span class="headline__char">地</span>
      <span class="headline__char">あ</span>
      <span class="headline__char">り</span>
      <span class="headline__char">ま</span>
      <span class="headline__char">す</span>
    </h2>

    <div class="brand-mark">
      <span class="brand-mark__dot"></span>
      <span class="brand-mark__name">碧浜ソレイユ</span>
    </div>

    <p class="company">碧浜ソレイユ株式会社</p>

    <div class="contact-bar">
      <svg class="contact-bar__icon" viewBox="0 0 100 80" aria-hidden="true">
        <path d="M8 30 C8 12 92 12 92 30 L92 36 L70 36 L70 28 L30 28 L30 36 L8 36 Z" fill="#ffffff"/>
        <path d="M22 42 L78 42 L88 74 L12 74 Z" fill="#ffffff"/>
        <circle cx="50" cy="58" r="9" fill="#0b5aa8"/>
      </svg>
      <span class="contact-bar__number">0995-61-2348</span>
    </div>
  </main>
</body>
</html>
```